Chill Bo
frozen yogurt and more
Corporate
Tara Kessler
Owner
4182 Larkspur Ln.
Columbus IN. 47358
tarasglow@quillpost.com
Don't have store open yet so have no address or phone numbers. We want logo font the same but would like a standard clean font for the rest of the info

```html
<!DOCTYPE html>
<html lang="en">
<head>
<meta charset="utf-8">
<title>Chill Bo – Business Cards</title>
<link rel="stylesheet" href="https://fonts.googleapis.com/css2?family=Open+Sans:wght@400;600;700&display=swap">
<style>
  :root {
    --backdrop: #e9d6b9;
    --card: #ffffff;
    --brown: #5b3a1e;
    --green: #8cc63f;
    --text: #4a3a2e;
    --muted: #7a6a5e;
    --divider: #c9c1b9;
    --pink: #e5197e;
  }
  * { margin: 0; padding: 0; box-sizing: border-box; }
  html, body { width: 1200px; height: 852px; overflow: hidden; }
  body {
    background: var(--backdrop);
    font-family: "Open Sans", Arial, sans-serif;
    color: var(--text);
    position: relative;
  }
  .card {
    position: absolute;
    width: 520px;
    height: 300px;
    background: var(--card);
    border-radius: 22px;
    overflow: hidden;
    box-shadow: 0 6px 18px rgba(60, 40, 20, 0.18);
  }
  .card--horizontal { left: 70px; top: 70px; }
  .card--centered { left: 610px; top: 480px; }
  .card__band { position: absolute; left: 0; top: 0; width: 520px; height: 120px; }
  .card__holder {
    position: absolute;
    right: 26px;
    top: 20px;
    text-align: right;
    color: #fff;
  }
  .card__name { font-size: 17px; font-weight: 700; line-height: 1.2; }
  .card__role { font-size: 11px; font-weight: 400; }
  .brand { display: flex; flex-direction: column; align-items: center; }
  .brand__row { display: flex; align-items: center; gap: 10px; }
  .brand__dot { width: 26px; height: 26px; border-radius: 50%; background: var(--pink); }
  .brand__name { font-size: 40px; font-weight: 600; color: var(--brown); line-height: 1.1; }
  .brand__tagline {
    font-size: 13px;
    letter-spacing: 3px;
    color: var(--green);
    font-weight: 600;
    margin-top: 2px;
  }
  .card--horizontal .brand { position: absolute; left: 26px; top: 150px; }
  .card__divider {
    position: absolute;
    left: 258px;
    top: 140px;
    width: 1px;
    height: 120px;
    background: var(--divider);
  }
  .contact { position: absolute; left: 282px; top: 145px; font-size: 12px; line-height: 1.5; }
  .contact__address { margin-bottom: 22px; }
  .contact__line { display: flex; align-items: center; gap: 8px; }
  .contact__line svg { width: 12px; height: 12px; flex: none; }
  .card--centered .brand { position: absolute; left: 0; right: 0; top: 118px; }
  .card--centered .brand__name { font-size: 36px; }
  .contact--centered {
    left: 0;
    right: 0;
    top: 206px;
    text-align: center;
    font-size: 12px;
    line-height: 1.55;
  }
  .contact--centered .contact__address { margin: 6px 0 0; }
</style>
</head>
<body>

<section class="card card--horizontal" aria-label="Business card, horizontal layout">
  <svg class="card__band" viewBox="0 0 520 120" aria-hidden="true">
    <path d="M0 0 H520 V96 C400 54 230 60 0 108 Z" fill="var(--brown)"/>
    <path d="M0 108 C230 60 400 54 520 96" fill="none" stroke="var(--green)" stroke-width="4"/>
  </svg>
  <div class="card__holder">
    <div class="card__name">Tara Kessler</div>
    <div class="card__role">Owner</div>
  </div>
  <div class="brand">
    <div class="brand__row">
      <span class="brand__dot"></span>
      <span class="brand__name">Chill Bo</span>
    </div>
    <span class="brand__tagline">FROZEN YOGURT</span>
  </div>
  <div class="card__divider"></div>
  <div class="contact">
    <div class="contact__address">4182 Larkspur Ln.<br>Columbus IN. 47358</div>
    <div class="contact__line">
      <svg viewBox="0 0 12 12" aria-hidden="true"><path d="M2 1 L4.5 1 L5.2 3.6 L3.8 4.6 C4.5 6.2 5.8 7.5 7.4 8.2 L8.4 6.8 L11 7.5 L11 10 C6 10.5 1.5 6 2 1 Z" fill="var(--text)"/></svg>
      <span>1-812-555-0147</span>
    </div>
    <div class="contact__line">
      <svg viewBox="0 0 12 12" aria-hidden="true"><rect x="1" y="2.5" width="10" height="7" rx="1" fill="none" stroke="var(--text)" stroke-width="1.2"/><path d="M1.5 3 L6 6.5 L10.5 3" fill="none" stroke="var(--text)" stroke-width="1.2"/></svg>
      <span>tarasglow@quillpost.com</span>
    </div>
  </div>
</section>

<section class="card card--centered" aria-label="Business card, centred layout">
  <svg class="card__band" viewBox="0 0 520 120" aria-hidden="true">
    <path d="M0 0 H520 V78 C400 44 230 50 0 92 Z" fill="var(--brown)"/>
    <path d="M0 92 C230 50 400 44 520 78" fill="none" stroke="var(--green)" stroke-width="4"/>
  </svg>
  <div class="card__holder">
    <div class="card__name">Tara Kessler</div>
    <div class="card__role">Owner</div>
  </div>
  <div class="brand">
    <div class="brand__row">
      <span class="brand__dot"></span>
      <span class="brand__name">Chill Bo</span>
    </div>
    <span class="brand__tagline">FROZEN YOGURT</span>
  </div>
  <div class="contact contact--centered">
    <div>1-812-555-0147</div>
    <div>tarasglow@quillpost.com</div>
    <div class="contact__address">4182 Larkspur Ln. Columbus IN. 47358</div>
  </div>
</section>

</body>
</html>
```